The Lindenmoor Compass Book

Cover Design for my first book. The book is for elementary school principals who are unhappy and are considering a career change but are afraid to leave. I teach them how to develop emotional fitness and resiliency through thought management so that they can decide whether to stay or leave their position from a place of empowerment. I've attached my podcast artwork for your reference. My publisher suggested not having me on the cover which is fine. I just thought it might be helpful.

Target Market(s)

Elementary School Principals

Industry/Entity Type

Education

Logo Text

The Lindenmoor Compass

Font styles to use
Serif
Sans Serif

Colors
34a6d7
33b8a4
3276b5

Requirements
Must have
• Title, Author name, photo or artwork that captures the essence of the book

```html
<!DOCTYPE html>
<html lang="en">
<head>
<meta charset="UTF-8">
<title>The Lindenmoor Compass – Book Cover</title>
<link rel="stylesheet" href="https://fonts.googleapis.com/css2?family=Oswald:wght@300;400;600&family=Jost:wght@300;400&display=swap">
<style>
  :root {
    --page-bg: #f3f4f6;
    --cover-top: #ead2de;
    --cover-mid: #f1e4ea;
    --cover-bottom: #ffffff;
    --title-blue: #2f9ad6;
    --title-ink: #1c1c1c;
    --band-blue: #1487c9;
    --band-text: #ffffff;
    --scene-pink: #ecdbe3;
    --scene-white: #f7f5f6;
    --scene-blue: #3fa6dd;
    --scene-yellow: #f3dc2e;
  }
  * { margin: 0; padding: 0; box-sizing: border-box; }
  html, body {
    width: 1200px;
    height: 800px;
    overflow: hidden;
    background: var(--page-bg);
  }
  .canvas {
    width: 1200px;
    height: 800px;
    display: flex;
    align-items: center;
    justify-content: center;
  }
  .book-cover {
    position: relative;
    width: 540px;
    height: 724px;
    background: linear-gradient(180deg, var(--cover-top) 0%, var(--cover-mid) 45%, var(--cover-bottom) 82%);
    overflow: hidden;
  }
  .title-block {
    position: absolute;
    top: 96px;
    left: 0;
    right: 0;
    padding-left: 80px;
    padding-right: 40px;
    text-align: center;
  }
  .title-article {
    font-family: 'Jost', sans-serif;
    font-weight: 400;
    font-size: 17px;
    letter-spacing: 6px;
    color: var(--title-ink);
    margin-bottom: 6px;
  }
  .title-main {
    font-family: 'Oswald', sans-serif;
    font-weight: 600;
    font-size: 68px;
    line-height: 1;
    letter-spacing: 2px;
    color: var(--title-blue);
  }
  .title-sub {
    font-family: 'Jost', sans-serif;
    font-weight: 300;
    font-size: 66px;
    line-height: 1.1;
    letter-spacing: 16px;
    margin-right: -16px;
    color: var(--title-ink);
  }
  .cover-art {
    position: absolute;
    top: 360px;
    left: 0;
    width: 540px;
    height: 266px;
    display: block;
  }
  .author-band {
    position: absolute;
    top: 626px;
    left: 0;
    right: 0;
    height: 56px;
    background: var(--band-blue);
    display: flex;
    align-items: center;
    justify-content: center;
  }
  .author-name {
    font-family: 'Oswald', sans-serif;
    font-weight: 300;
    font-size: 29px;
    letter-spacing: 2.5px;
    color: var(--band-text);
    padding-left: 40px;
  }
</style>
</head>
<body>
  <main class="canvas">
    <section class="book-cover">
      <header class="title-block">
        <p class="title-article">THE</p>
        <h1 class="title-main">LINDENMOOR</h1>
        <p class="title-sub">COMPASS</p>
      </header>

      <svg class="cover-art" viewBox="0 0 540 266" role="img" aria-label="Photograph of a row of blue balls with sad faces and one yellow ball with a smile on a soft pink and white surface">
        <defs>
          <linearGradient id="artSurface" x1="0" y1="0" x2="0" y2="1">
            <stop offset="0" stop-color="var(--scene-pink)" stop-opacity="0"/>
            <stop offset="0.45" stop-color="var(--scene-pink)"/>
            <stop offset="1" stop-color="var(--scene-white)"/>
          </linearGradient>
          <linearGradient id="artTones" x1="0" y1="0" x2="1" y2="0">
            <stop offset="0.05" stop-color="var(--scene-blue)" stop-opacity="0"/>
            <stop offset="0.22" stop-color="var(--scene-blue)" stop-opacity="0.35"/>
            <stop offset="0.38" stop-color="var(--scene-yellow)" stop-opacity="0.35"/>
            <stop offset="0.58" stop-color="var(--scene-blue)" stop-opacity="0.3"/>
            <stop offset="0.8" stop-color="var(--scene-blue)" stop-opacity="0"/>
          </linearGradient>
        </defs>
        <rect x="0" y="0" width="540" height="266" fill="url(#artSurface)"/>
        <rect x="0" y="20" width="540" height="160" fill="url(#artTones)"/>
      </svg>

      <div class="author-band">
        <p class="author-name">MARISA HALE CORWIN</p>
      </div>
    </section>
  </main>
</body>
</html>
```